Dermatology in Your Lane Logo and business card

We provide dermatological services to the community. This includes Assisted Living Facilities, nursing homes and to large cooperation, Health fairs etc. We provide a health care provider that travels to institutions, providing these services. All procedures and surgeries are done onsite in one of our state of the art mobile clinics. We provide services including, but not limited to; skin biopsies, skin surgeries , surgical procedures including skin cancer removal mole removal and treatment of various skin disorders. we bring mobile Dermatology to you.

Industry/Entity Type

Business

Contact Information for Business Card

Need Logo address phone number, email website

Logo Text

Dermatology in Your Lane

Logo styles of interest
Emblem Logo
Abstract Logo
Character Logo
Lettermark Logo
Requirements
Must have
• Marcus Penhale ARNP DN-C
• Medical Facilitator
• P. (407) 555-3194
• Fax (386) 555-7721

```html
<!DOCTYPE html>
<html lang="en">
<head>
<meta charset="utf-8">
<title>Dermatology in Your Lane — Business Card</title>
<link rel="stylesheet" href="https://fonts.googleapis.com/css2?family=Cinzel:wght@400;600;700&display=swap">
<style>
  :root {
    --page-bg: #ffffff;
    --card-front: #ffffff;
    --card-back: #4dadd4;
    --card-border: #8d8d8d;
    --brand-blue: #1d5a92;
    --brand-blue-deep: #1c4f86;
    --text-blue: #2a5d93;
    --badge-navy: #1b3763;
    --shadow: rgba(0, 0, 0, 0.28);
  }
  * { margin: 0; padding: 0; box-sizing: border-box; }
  html, body {
    width: 1200px;
    height: 1200px;
    overflow: hidden;
    background: var(--page-bg);
  }
  .sheet {
    position: relative;
    width: 1200px;
    height: 1200px;
    font-family: "Cinzel", "Times New Roman", serif;
  }
  .card {
    position: absolute;
    left: 320px;
    width: 550px;
    height: 310px;
    box-shadow: 8px 10px 12px var(--shadow);
  }
  .card--front {
    top: 177px;
    background: var(--card-front);
    border: 1.5px solid var(--card-border);
  }
  .card--back {
    top: 607px;
    background: var(--card-back);
  }
  .brand-name {
    position: absolute;
    left: 0;
    right: 0;
    text-align: center;
    font-weight: 700;
    font-size: 25px;
    letter-spacing: 0.3px;
    white-space: nowrap;
    color: var(--brand-blue);
  }
  .card--front .brand-name { top: 76px; left: -22px; }
  .card--back .brand-name { top: 80px; left: -22px; color: var(--brand-blue-deep); }

  .holder {
    position: absolute;
    left: 20px;
    top: 196px;
    width: 240px;
    text-align: center;
    color: var(--text-blue);
  }
  .holder__name {
    font-size: 25px;
    font-weight: 600;
    line-height: 1;
  }
  .holder__credentials {
    margin-top: 8px;
    font-size: 12px;
    letter-spacing: 1px;
    line-height: 1;
  }
  .holder__role {
    margin-top: 13px;
    font-size: 16px;
    font-weight: 700;
    line-height: 1;
  }

  .contact {
    position: absolute;
    left: 335px;
    top: 238px;
    list-style: none;
    color: var(--text-blue);
  }
  .contact__item {
    display: flex;
    align-items: center;
    height: 17px;
    margin-bottom: 8px;
    font-size: 13px;
  }
  .contact__badge {
    width: 17px;
    height: 17px;
    background: var(--badge-navy);
    color: #ffffff;
    font-size: 11px;
    font-weight: 700;
    display: flex;
    align-items: center;
    justify-content: center;
    margin-right: 14px;
  }
</style>
</head>
<body>
  <main class="sheet">
    <section class="card card--front" aria-label="Business card front">
      <div class="brand-name">Dermatology in Your Lane</div>
      <div class="holder">
        <div class="holder__name">Marcus Penhale</div>
        <div class="holder__credentials">ARNP DN-C</div>
        <div class="holder__role">Medical Facilitator</div>
      </div>
      <ul class="contact">
        <li class="contact__item"><span class="contact__badge">P</span>- P. (407) 555-3194</li>
        <li class="contact__item"><span class="contact__badge">E</span>- Fax (386) 555-7721</li>
      </ul>
    </section>
    <section class="card card--back" aria-label="Business card back">
      <div class="brand-name">Dermatology in Your Lane</div>
    </section>
  </main>
</body>
</html>
```